Harbor Business Cards

I need a business card designed with the following information.

Company Name: Harbor Wealth Management
Name: BriAnne Dockery
Title: Executive Assistant
Cell: (281) 555-0173
Direct Line: (832) 555-0148
Email: brianne@harborwmx.com
Address: 20537 W. Marlowe PKWY Ste. B
Tomball, TX 77390

I have attached the logo.
I would like it in navy blue and silver.
Thanks.

```html
<!DOCTYPE html>
<html lang="en">
<head>
<meta charset="utf-8">
<title>Harbor Wealth Management — Business Card</title>
<link rel="stylesheet" href="https://fonts.googleapis.com/css2?family=Alegreya+Sans:wght@400;700&display=swap">
<style>
  :root {
    --backdrop: #282828;
    --navy: #0e2240;
    --silver: #b9b9bb;
    --paper: #ffffff;
    --ink: #2a2a2a;
  }
  html, body {
    margin: 0;
    width: 1200px;
    height: 1200px;
    overflow: hidden;
    background: var(--backdrop);
    font-family: "Alegreya Sans", sans-serif;
  }
  .card {
    position: absolute;
    left: 214px;
    width: 772px;
    height: 442px;
    border-radius: 30px;
    overflow: hidden;
  }
  .card--front { top: 130px; background: var(--navy); }
  .card--back  { top: 615px; background: var(--paper); }

  .brand {
    position: absolute;
    text-align: center;
    font-weight: 400;
    text-transform: uppercase;
    margin: 0;
    line-height: 1;
  }
  .card--front .brand {
    left: 0; right: 0; top: 260px;
    color: var(--silver);
  }
  .card--back .brand {
    left: 110px; width: 240px; top: 247px;
    color: var(--navy);
  }
  .brand__name { display: block; letter-spacing: 0.62em; padding-left: 0.62em; }
  .brand__sub { display: block; letter-spacing: 0.32em; padding-left: 0.32em; margin-top: 14px; }
  .card--front .brand__name { font-size: 42px; }
  .card--front .brand__sub { font-size: 16px; }
  .card--back .brand__name { font-size: 29px; }
  .card--back .brand__sub { font-size: 11px; margin-top: 10px; }

  .rule {
    position: absolute;
    left: 376px;
    width: 1.5px;
    background: var(--navy);
  }
  .details { position: absolute; left: 404px; color: var(--ink); font-size: 19px; line-height: 23px; letter-spacing: 0.02em; }
  .person { top: 124px; }
  .person__name { margin: 0; color: var(--navy); font-weight: 700; font-size: 27px; line-height: 28px; letter-spacing: 0.05em; text-transform: uppercase; }
  .person__title { margin: 0; line-height: 20px; }
  .address { top: 180px; font-style: normal; }
  .contacts { top: 233px; list-style: none; margin: 0; padding: 0; }
  .contacts li { display: flex; align-items: center; height: 24px; }
  .contacts svg { width: 16px; height: 16px; margin-right: 10px; fill: var(--navy); flex: none; }
</style>
</head>
<body>
  <section class="card card--front">
    <p class="brand"><span class="brand__name">Harbor</span><span class="brand__sub">Wealth Management</span></p>
  </section>

  <section class="card card--back">
    <p class="brand"><span class="brand__name">Harbor</span><span class="brand__sub">Wealth Management</span></p>

    <span class="rule" style="top:125px;height:38px"></span>
    <span class="rule" style="top:182px;height:33px"></span>
    <span class="rule" style="top:235px;height:88px"></span>

    <div class="details person">
      <h1 class="person__name">BriAnne Dockery</h1>
      <p class="person__title">Executive Assistant</p>
    </div>

    <address class="details address">20537 W. Marlowe PKWY Ste. B<br>Tomball, TX 77390</address>

    <ul class="details contacts">
      <li><svg viewBox="0 0 16 16"><path d="M4 1h8v14H4zM5.5 3v4h5V3zM5.5 9h1.5v1.3H5.5zm2.3 0h1.5v1.3H7.8zm2.3 0h1.5v1.3h-1.5zM5.5 11.3h1.5v1.3H5.5zm2.3 0h1.5v1.3H7.8zm2.3 0h1.5v1.3h-1.5z" fill-rule="evenodd"/></svg>(281) 555-0173</li>
      <li><svg viewBox="0 0 16 16"><path d="M3.5 1.5l2.5 3-1.5 1.8c.8 2 2.3 3.5 4.2 4.2L10.5 9l3 2.5-1.8 2.5C6.5 13.5 2.5 9.5 2 4.3z"/></svg>(832) 555-0148</li>
      <li><svg viewBox="0 0 16 16"><path d="M1 4h14v1.2L8 9.5 1 5.2zM1 6.6l7 4.3 7-4.3V13H1z"/></svg>brianne@harborwmx.com</li>
      <li><svg viewBox="0 0 16 16" fill="none" stroke="#0e2240" stroke-width="1.2"><circle cx="8" cy="8" r="6.3"/><ellipse cx="8" cy="8" rx="2.8" ry="6.3"/><path d="M1.7 8h12.6M2.7 5h10.6M2.7 11h10.6"/></svg>www.harborwmx.com</li>
    </ul>
  </section>
</body>
</html>
```